Medical equipment business looking for professional, unique business card

We need a business card design for a durable medical equipment company. We are small but would like our cards to express that we are much bigger. We focus on braces (back, knee, wrist, etc) but also do crutches, rollators, wheelchairs- basically medical equipment that gets you going and back in Action. Our colors are blue and green and our logo has an arrow and use of a "spine". We'd like to express professionalism while being unique.

Industry/Entity Type

Medical Equipment

Contact Information for Business Card

Professional feel but unique. Memorable.

Font styles to use
Serif
Sans Serif
Other font styles liked:
• verdana

Requirements
Must have
• card holders cell#, business phone#, fax#, email, website address, business address, logo
Nice to have
• use of medical/healthcare related descriptive words, items, look
Should not have
• the wrong colors or cartoon characters.

```html
<!DOCTYPE html>
<html lang="en">
<head>
<meta charset="utf-8">
<title>Stridewell DME – Business Card</title>
<link href="https://fonts.googleapis.com/css2?family=Noto+Sans:wght@400;600;700&display=swap" rel="stylesheet">
<style>
  :root {
    --backdrop: #5b4b3d;
    --card-white: #ffffff;
    --brand-blue: #0b4a70;
    --band-blue: #004a70;
    --brand-green: #8dc63f;
    --text-grey: #555a5f;
    --icon-blue: #1d4d6c;
  }
  html, body {
    margin: 0;
    padding: 0;
    width: 1200px;
    height: 987px;
    overflow: hidden;
    background: var(--backdrop);
    font-family: "Noto Sans", Verdana, sans-serif;
  }
  .canvas {
    position: relative;
    width: 1200px;
    height: 987px;
  }
  .card {
    position: absolute;
    left: 293px;
    width: 615px;
    height: 352px;
    overflow: hidden;
  }
  .card--front { top: 130px; background: var(--card-white); }
  .card--back { top: 505px; background: var(--brand-green); }

  .brand-name {
    position: absolute;
    margin: 0;
    font-weight: 600;
    color: var(--brand-blue);
    white-space: nowrap;
    line-height: 1;
    display: flex;
    align-items: center;
    gap: 12px;
  }
  .brand-mark {
    width: 18px;
    height: 18px;
    border-radius: 50%;
    background: var(--brand-green);
    flex: none;
  }
  .card--front .brand-name { left: 39px; top: 48px; font-size: 32px; }
  .card--back .brand-name {
    left: 50%;
    top: 50%;
    transform: translate(-50%, -50%);
    font-size: 44px;
  }
  .card--back .brand-mark { width: 24px; height: 24px; background: var(--brand-blue); }

  .address {
    position: absolute;
    left: 39px;
    top: 135px;
    margin: 0;
    font-style: normal;
    font-size: 16px;
    line-height: 20px;
    color: var(--text-grey);
  }
  .contacts {
    position: absolute;
    left: 39px;
    top: 186px;
    margin: 0;
    padding: 0;
    list-style: none;
    font-size: 16px;
    color: var(--text-grey);
  }
  .contacts li {
    display: flex;
    align-items: center;
    height: 23.5px;
  }
  .contacts svg {
    width: 15px;
    height: 15px;
    margin-right: 8px;
    fill: var(--icon-blue);
    flex: none;
  }
  .holder {
    position: absolute;
    right: 49px;
    top: 190px;
    text-align: right;
  }
  .holder-name {
    margin: 0;
    font-size: 23px;
    font-weight: 700;
    color: var(--brand-blue);
    line-height: 30px;
  }
  .holder-title {
    margin: 0;
    font-size: 17px;
    color: var(--brand-green);
    line-height: 24px;
  }
  .swoosh {
    position: absolute;
    left: 0;
    top: 300px;
    width: 615px;
    height: 36px;
  }
  .base-band {
    position: absolute;
    left: 0;
    bottom: 0;
    width: 100%;
    height: 26px;
    background: var(--band-blue);
  }
</style>
</head>
<body>
<main class="canvas">
  <section class="card card--front" aria-label="Business card front">
    <p class="brand-name"><span class="brand-mark"></span>Stridewell DME</p>

    <address class="address">4120 Alder Court<br>Juneau, Alaska 99801</address>

    <ul class="contacts">
      <li><svg viewBox="0 0 16 16" aria-hidden="true"><path d="M3.5 1l2.6 3-1.4 1.8c.9 2 2.5 3.6 4.5 4.5L11 8.9l3 2.6-1.3 2.6c-.4.7-1.2 1-2 .8C6 13.6 2.4 10 1.1 5.3.9 4.5 1.2 3.7 1.9 3.3z"/></svg>907 555 0142</li>
      <li><svg viewBox="0 0 16 16" aria-hidden="true"><path d="M4.5 0h7c.8 0 1.5.7 1.5 1.5v13c0 .8-.7 1.5-1.5 1.5h-7C3.7 16 3 15.3 3 14.5v-13C3 .7 3.7 0 4.5 0zM5 2v10.5h6V2zm3 11.2a.9.9 0 100 1.8.9.9 0 000-1.8z"/></svg>907 555 0187</li>
      <li><svg viewBox="0 0 16 16" aria-hidden="true"><path d="M4 1h8v4H4zM1.5 6h13c.8 0 1.5.7 1.5 1.5V13H0V7.5C0 6.7.7 6 1.5 6zM3 8v1.5h2V8zm1 3v1h8v-1zm-4 3h16v1.5H0z"/></svg>907 555 0163</li>
      <li><svg viewBox="0 0 16 16" aria-hidden="true"><path d="M0 3h16v1.2L8 9 0 4.2zm0 2.6l8 4.8 8-4.8V13H0z"/></svg>name@stridewelldme.com</li>
      <li><svg viewBox="0 0 16 16" aria-hidden="true"><path d="M8 0a8 8 0 100 16A8 8 0 008 0zm-1 2.2c-.8.7-1.8 1-1.8 2 0 .8 1 1 1.3 1.8.3.9-.7 1.4-.3 2.3.4.8 1.5.6 1.8 1.6.2.9-.5 2-.1 3.3-2.9-.5-5-3-5-5.9 0-2.6 1.7-4.8 4.1-5.6zm3.3.4c1.6.8 2.8 2.3 3.2 4.1-.6-.3-1.3-.1-1.8.4-.6.6-1.4.2-1.7-.5-.3-.8.5-1.4.3-2.4z"/></svg>www.stridewelldme.com</li>
    </ul>

    <div class="holder">
      <p class="holder-name">Daniel Reyes</p>
      <p class="holder-title">CEO/Founder</p>
    </div>

    <svg class="swoosh" viewBox="0 0 615 36" aria-hidden="true">
      <path d="M0 24 L570 14 L570 20 Z" fill="var(--brand-green)"/>
      <path d="M555 3 L588 17 L555 31 L562 17 Z" fill="var(--brand-green)" stroke="#ffffff" stroke-width="2" stroke-linejoin="round"/>
    </svg>
    <div class="base-band"></div>
  </section>

  <section class="card card--back" aria-label="Business card back">
    <p class="brand-name"><span class="brand-mark"></span>Stridewell DME</p>
  </section>
</main>
</body>
</html>
```